Tri-Fold Menu of Services for our Eyelash and Skin Care Spa

We need a beautiful spa service menu for our upscale spa in St. Charles Missouri. We specialize in providing treatments that are specific to the clients needs. Our services are eyelash extensions, skin care treatments, full body waxing and makeup application. Our spa colors are dark purples and greys and we are not opposed to additional colors that would complement those colors. We do a lot of eyelash extensions and while we do what those services listed we would like the skin care treatments to be in an area that would be noticed first. One of the attachments lists all of our services, descriptions and prices (please be sure to include all services and pricing. descriptions if possible). And our website has more information about us if needed. The website was not professionally done. So it DOESN'T represent our style exactly.

I HAVE ATTACHED A FEW PHOTOS BUT THEY DON'T HAVE TO BE USED.

Target Market(s)

women who would like to look their best, 35-55, annual income of 100,000+, she is usually busy and her children (if she has any) are high school age or older.

Industry/Entity Type

It Service

Font styles to use
Serif
Sans Serif

Requirements
Must have
• Must list all of our services. If it works to have the descriptions that would be great.
Nice to have
• If it works to have the descriptions of each service that would be great.

```html
<!DOCTYPE html>
<html lang="en">
<head>
<meta charset="utf-8">
<title>Spa Menu of Services</title>
<link href="https://fonts.googleapis.com/css2?family=Archivo+Black&family=Roboto+Condensed:wght@400;700&family=Arimo:wght@400&display=swap" rel="stylesheet">
<style>
:root{
  --ink:#2a1c33;
  --heading:#3b2150;
  --body-ink:#4a4450;
  --lavender-light:#f1edf4;
  --lavender:#ddd3e6;
  --purple-grey:#c3b6cf;
  --grey-top:#e8e6ec;
  --fold:#9c91a6;
  --accent:#5d3a78;
  --page:#ffffff;
}
*{box-sizing:border-box;margin:0;padding:0}
html,body{width:1200px;height:1102px;overflow:hidden;background:var(--page)}
.menu{display:flex;width:1200px;height:1102px}
.panel{position:relative;width:400px;height:1102px;overflow:hidden;
  background:linear-gradient(180deg,var(--lavender-light) 0%,var(--lavender) 60%,var(--purple-grey) 100%);
  border-right:1px solid var(--fold);color:var(--ink)}
.panel:last-child{border-right:none}
.panel--center{background:linear-gradient(180deg,var(--grey-top) 0%,var(--lavender-light) 30%,var(--lavender) 70%,var(--purple-grey) 100%)}
.pattern{position:absolute;inset:0;
  background:radial-gradient(circle at 30% 20%,rgba(255,255,255,.55),transparent 45%),
             radial-gradient(circle at 75% 70%,rgba(255,255,255,.35),transparent 50%),
             linear-gradient(160deg,rgba(120,110,135,.12),transparent 60%)}
.content{position:absolute;inset:0}
.heading{font-family:"Archivo Black",Arial,sans-serif;font-size:21px;letter-spacing:.5px;text-align:center;position:absolute;left:0;right:0;color:var(--heading)}
.heading--plain{font-family:"Roboto Condensed",Arial,sans-serif;font-weight:700;font-size:21px;letter-spacing:0}
.subhead{font-family:"Roboto Condensed",Arial,sans-serif;font-weight:700;font-size:17px;position:absolute;color:var(--heading)}
.service{position:absolute;left:10px;right:12px}
.service__row{display:flex;justify-content:space-between;gap:8px;font-family:"Roboto Condensed",Arial,sans-serif;font-weight:700;font-size:16px;line-height:19px}
.service__price{font-weight:400;white-space:nowrap}
.service__desc{font-family:Arimo,Arial,sans-serif;font-size:9.5px;line-height:12px;color:var(--body-ink);margin-top:2px}
.list{position:absolute;font-family:"Roboto Condensed",Arial,sans-serif;font-weight:700;font-size:15.5px;line-height:18.6px}
.list__row{display:flex;justify-content:space-between}
.list__row span:last-child{font-weight:400}
.list__price{width:110px}
.peel{position:absolute;left:12px;right:20px}
.peel .service__row{font-size:15px}
.peel .service__desc{font-size:8.5px}
.rule{position:absolute;left:60px;right:60px;height:1px;background:var(--accent);opacity:.5}
</style>
</head>
<body>
<main class="menu">

  <section class="panel panel--left">
    <div class="pattern" role="img" aria-label="Soft blossom and bamboo leaf pattern"></div>
    <div class="content">
      <h2 class="heading" style="top:125px">FACIAL &amp; SKIN TREATMENTS</h2>

      <article class="service" style="top:170px">
        <div class="service__row"><span>Essential Deep Cleansing Treatment</span><span class="service__price">$65 60 minutes</span></div>
        <p class="service__desc">This relaxing, purifying treatment consists of steaming, exfoliation, and an intense deeper cleansing of clogged pores. A skintype specific ampoule is gently massaged into the skin of your face, neck, and decollete, followed by a therapist selected mask. Beneficial for all skin types.</p>
      </article>

      <article class="service" style="top:262px">
        <div class="service__row"><span>Mini Facial</span><span class="service__price">$48 30 minutes</span></div>
        <p class="service__desc">This express facial is ideal for those on the go. Your skin is cleansed, lightly exfoliated and gently massaged. A porerefining mask is then applied, followed by a veil of light moisturizer.</p>
      </article>

      <article class="service" style="top:330px">
        <div class="service__row"><span>Aromatherapy Facial</span><span class="service__price">$75 60 minutes</span></div>
        <p class="service__desc">Our Aromatherapy facial will naturally enhance the facial benefits using fragrant oils extracted from flowers, fruits and herbs.</p>
      </article>

      <article class="service" style="top:388px">
        <div class="service__row"><span>Lumiva Lift &amp; Glow Treatment Facial</span><span class="service__price">$95 60 minutes</span></div>
        <p class="service__desc">Seeking a treatment with amazing instant results? Redefining radiance and facial contouring, this exclusively formulated treatment features the latest in freezedried technology to deliver instant results and cumulative skin care benefits. Ideal for any skin type showing signs of aging, or as the perfect instant repair boost when you want to look your best. Proven to perform, the Verelle Lumiva Lift &amp; Glow facial renders your skin ultraluminous with a firmer, tighter, and more youthfully defined appearance.</p>
      </article>

      <article class="service" style="top:525px">
        <div class="service__row"><span>Soothing Plantomer Treatment Facial</span><span class="service__price">$100 60 minutes</span></div>
        <p class="service__desc">This highly effective, soothing treatment calms redness and alleviates irritated or sensitive skin. A healing Propolis ampoule (natural ingredient collected by bees) is applied to desensitize the skin's surface and strengthen capillaries. A cooling liftoff mask is then applied to seal in the vitamin enriched beneficial ampoule.</p>
      </article>

      <article class="service" style="top:612px">
        <div class="service__row"><span>Radiance PhotoTherapy Treatment<br>8/$800</span><span class="service__price">$150 Package</span></div>
        <p class="service__desc">Uses heat and light energy to gently break up areas of excess pigment while stimulating the production of new collagen. Improved skin tone, less spots, fewer pink areas, less redness, reduction in fine lines and wrinkles. Diminishes pores and restores natural radiant glow of skin. Like laser treatments MicroPhotoTherapy treats skin with therapeutic light energy but unlike laser treatments, Micro PhotoTherapy features gentle waves of heat and light that improve the skin with no downtime and very little discomfort. We recommend 8 treatments 1 to 2 times a week for best results.</p>
      </article>

      <article class="service" style="top:770px">
        <div class="service__row"><span>Diamond Microdermabrasion Treatment</span><span class="service__price">$78</span></div>
        <p class="service__desc">With this treatment you will see softening of fine lines and wrinkles and smoothing of coarsely textured skin. Dull, stressed or congested skin will be brighter and clearer. The appearance of enlarged pores, and acne scars will be minimized. Your at home products will be able to penetrate deeper therefore, are more effective. Or add this to any facial or most peels for just $30.</p>
      </article>
    </div>
  </section>

  <section class="panel panel--center">
    <div class="pattern" role="img" aria-label="Soft blossom petal pattern"></div>
    <div class="content">
      <h2 class="heading heading--plain" style="top:140px">Peels</h2>

      <article class="peel" style="top:192px">
        <div class="service__row"><span>Acne Lift Peel</span><span class="service__price">$50/1 $250/6 30 minutes</span></div>
        <p class="service__desc">Mild to moderate Acne peel</p>
      </article>
      <article class="peel" style="top:236px">
        <div class="service__row"><span>Lightening Lift Peel</span><span class="service__price">$50/1 $250/6 30 minutes</span></div>
        <p class="service__desc">Pigmentation (sun/brown spots), uneven skin tone</p>
      </article>
      <article class="peel" style="top:280px">
        <div class="service__row"><span>Wrinkle Lift</span><span class="service__price">$50/1 $250/6 30 minutes</span></div>
        <p class="service__desc">Aging, fine lines and wrinkles</p>
      </article>
      <article class="peel" style="top:324px">
        <div class="service__row"><span>Signature Lift</span><span class="service__price">$50/1 $250/6 30minutes</span></div>
        <p class="service__desc">Rosacea, dry/dehydrated</p>
      </article>
      <article class="peel" style="top:368px">
        <div class="service__row"><span>Perfection Lift</span><span class="service__price">$100/1 $350/4 30 minutes</span></div>
        <p class="service__desc">Advanced Aging, Acne, and Pigmentation (slightly more aggressive than the other options)</p>
      </article>

      <h2 class="heading heading--plain" style="top:530px">Add Ons</h2>
      <div class="list" style="top:562px;left:12px;right:80px">
        <div class="list__row"><span>Microdermabrasion</span><span>$30</span></div>
        <div class="list__row"><span>Lumiva Lift &amp; Glow Eye Treatment</span><span>$20</span></div>
        <div class="list__row"><span>Hot or Cold Stones</span><span>$15</span></div>
        <div class="list__row"><span>Extended Massage</span><span>$15</span></div>
        <div class="list__row"><span>Peppermint Scalp Massage</span><span>$15</span></div>
        <div class="list__row"><span>Foot Scrub &amp; Massage</span><span>$20</span></div>
        <div class="list__row"><span>Aromatherapy</span><span>$10</span></div>
        <div class="list__row"><span>Specialty Ampoule</span><span>$15</span></div>
        <div class="list__row"><span>Specialty Mask</span><span>$13</span></div>
      </div>
    </div>
  </section>

  <section class="panel panel--right">
    <div class="pattern" role="img" aria-label="Soft bamboo stalks and blossom pattern"></div>
    <div class="content">
      <h2 class="heading" style="top:140px;font-size:20px">EYELASHES</h2>

      <h3 class="subhead" style="top:215px;left:8px">Classic</h3>
      <div class="list" style="top:238px;left:95px;width:200px">
        <div class="list__row"><span>Full Set</span><span>175</span></div>
        <div class="list__row"><span>Demi Set</span><span>110</span></div>
        <div class="list__row"><span>Touch up</span><span>60</span></div>
      </div>

      <h3 class="subhead" style="top:335px;left:8px;font-size:15px">Volume Technique</h3>
      <div class="list" style="top:362px;left:95px;width:200px">
        <div class="list__row"><span>Full Set</span><span>220</span></div>
        <div class="list__row"><span>Demi Set</span><span>135</span></div>
        <div class="list__row"><span>Touch up</span><span>72</span></div>
      </div>

      <h2 class="heading" style="top:535px;font-size:20px">WAXING</h2>
      <div class="list" style="top:580px;left:95px;width:280px">
        <div class="list__row"><span>Eyebrows</span><span class="list__price">$17</span></div>
        <div class="list__row"><span>Upper Lip</span><span class="list__price">$14</span></div>
        <div class="list__row"><span>Chin</span><span class="list__price">$14</span></div>
        <div class="list__row"><span>Sides of face</span><span class="list__price">$14</span></div>
        <div class="list__row"><span>Bikini</span><span class="list__price">$27+</span></div>
        <div class="list__row"><span>Brazilian</span><span class="list__price">$55+</span></div>
        <div class="list__row"><span>Underarm</span><span class="list__price">$22</span></div>
        <div class="list__row"><span>Arms Full</span><span class="list__price">$35 Lower $26</span></div>
        <div class="list__row"><span>Legs Full</span><span class="list__price">$62 Lower $40</span></div>
        <div class="list__row"><span>Chest</span><span class="list__price">$44</span></div>
        <div class="list__row"><span>Back</span><span class="list__price">$44</span></div>
      </div>

      <div class="rule" style="top:820px"></div>
      <h2 class="heading" style="top:845px;font-size:20px">MAKEUP</h2>
      <div class="list" style="top:890px;left:95px;width:280px">
        <div class="list__row"><span>Makeup Application</span><span class="list__price">By consultation</span></div>
      </div>
    </div>
  </section>

</main>
</body>
</html>
```